New Podcast focussing on non-mainstream interventions for guidance needs podcast art

I need an exquisite piece of podcast art work for the launch of my new podcast 'Beyond the Still'. This podcast explores unorthodox, esoteric and unconventional methods to find peace, clarity and direction in life. Topics include family Constellations Systems, Psychedelics, Equine Therapy and Floatation to name a few. A teaser has been posted on Talvora with a strong response. The audience is primarily midlifers or those in a career/personal crisis of direction. It's meant to comfort, inform and empower and offer other ways rather than mainstream to work out what to do with your life. The file shared with you shows the pic used on Talvora as it's illustrating the idea of illumination. You can use it or not, and whilst I am ex-Military, I don't want the cover to convey an overly military influence. I'd like 'Beyond the Still' to feature on the art work and my name, Mirela Dunford. I'd like inspiration, creativity, and the idea of hope conveyed as well as clarity and courage. Whilst the podcast is about finding your direction please do no use compass images or cross road images as that is too obvious.
Hope that all helps. Looking forward to your ideas.

```html
<!DOCTYPE html>
<html lang="en">
<head>
<meta charset="utf-8">
<title>Beyond the Still – Podcast Cover</title>
<link href="https://fonts.googleapis.com/css2?family=EB+Garamond:wght@400;500&display=swap" rel="stylesheet">
<style>
  :root {
    --night: #050a18;
    --sky-teal: #1d4a50;
    --sky-deep: #0b1f2a;
    --glow: #bfe3da;
    --field: #a8641c;
    --field-dark: #3a2410;
    --frame: #ffffff;
    --accent: #f77f0f;
    --text: #ffffff;
  }
  html, body {
    margin: 0;
    padding: 0;
    width: 1200px;
    height: 1200px;
    overflow: hidden;
    background: var(--night);
  }
  .cover {
    position: relative;
    width: 1200px;
    height: 1200px;
    background: var(--night);
    font-family: "EB Garamond", Garamond, serif;
    color: var(--text);
    overflow: hidden;
  }
  .cover__artwork {
    position: absolute;
    inset: 0 0 auto 0;
    height: 820px;
    background:
      radial-gradient(ellipse 260px 230px at 600px 170px, rgba(191,227,218,0.75), rgba(60,120,120,0.35) 55%, transparent 80%),
      linear-gradient(180deg, var(--sky-deep) 0%, var(--sky-teal) 40%, #1b3a3c 52%, #20241c 58%, var(--field) 64%, var(--field-dark) 72%, var(--night) 100%);
  }
  .cover__frame {
    position: absolute;
    left: 43px;
    top: 45px;
    width: 1109px;
    height: 1095px;
    overflow: visible;
  }
  .cover__label {
    position: absolute;
    left: 0;
    right: 0;
    margin: 0;
    text-align: center;
    font-weight: 400;
    line-height: 1;
  }
  .cover__label--top {
    top: 27px;
    font-size: 33px;
    letter-spacing: 0.55em;
    text-indent: 0.55em;
  }
  .cover__label--bottom {
    top: 1120px;
    font-size: 34px;
    letter-spacing: 0.38em;
    text-indent: 0.38em;
  }
  .cover__title {
    position: absolute;
    inset: 0;
    width: 1200px;
    height: 1200px;
  }
  .title__lead {
    font-family: "EB Garamond", Garamond, serif;
    font-size: 92px;
    font-weight: 400;
    fill: var(--text);
  }
  .title__main {
    font-family: "EB Garamond", Garamond, serif;
    font-size: 418px;
    font-weight: 500;
    fill: var(--accent);
  }
</style>
</head>
<body>
  <main class="cover">
    <div class="cover__artwork" role="img" aria-label="Photograph of a woman with long hair seen from behind, sitting cross-legged on a blanket in a golden grassy field at night, gazing up at a glowing swirling starry sky"></div>

    <svg class="cover__frame" viewBox="0 0 1109 1095" aria-hidden="true">
      <g fill="none" stroke="var(--frame)" stroke-width="3">
        <polyline points="362,1.5 1.5,1.5 1.5,1093.5 272,1093.5"/>
        <polyline points="747,1.5 1107.5,1.5 1107.5,1093.5 842,1093.5"/>
      </g>
    </svg>

    <p class="cover__label cover__label--top">PODCAST</p>

    <svg class="cover__title" viewBox="0 0 1200 1200" role="heading" aria-level="1" aria-label="Beyond the Still">
      <text class="title__lead" x="600" y="761" text-anchor="middle">BEYOND THE</text>
      <text class="title__main" x="78" y="1078" textLength="1046" lengthAdjust="spacingAndGlyphs">STILL</text>
    </svg>

    <p class="cover__label cover__label--bottom">MIRELA DUNFORD</p>
  </main>
</body>
</html>
```